Property Management Company Business Cards

Need business cards for a property management company located in Michigan. We manage houses for clients all over the world. Young and modern company, looking for eye catching design. Please work with the attached logo.

Industry/Entity Type

Property Management

Requirements
Must have
• Need lines for address, telephone number, fax number, web site.

Also lines for name, and job title

```html
<!DOCTYPE html>
<html lang="en">
<head>
<meta charset="utf-8">
<title>Larkspur Homes – Business Cards</title>
<link href="https://fonts.googleapis.com/css2?family=Open+Sans:wght@400;600;700&display=swap" rel="stylesheet">
<style>
  :root {
    --stage: #3b2b20;
    --navy-deep: #06193a;
    --navy: #0b3a78;
    --blue-glow: #2a86c9;
    --blue-band: #0d4f95;
    --paper: #ececec;
    --paper-light: #f7f7f7;
    --silver: #c9cdd2;
    --ink: #1b1b1b;
    --ink-soft: #3a3a3a;
    --white: #ffffff;
    --rule: #2a2a2a;
  }
  * { margin: 0; padding: 0; box-sizing: border-box; }
  html, body {
    width: 1200px; height: 900px; overflow: hidden;
    background: var(--stage);
    font-family: "Open Sans", Arial, sans-serif;
  }
  .canvas { position: relative; width: 1200px; height: 900px; }
  .card {
    position: absolute; left: 250px; width: 700px; height: 400px;
    overflow: hidden; border-radius: 3px;
    box-shadow: 0 10px 30px rgba(0,0,0,.45);
  }
  .card--front { top: 35px; background:
      radial-gradient(ellipse 55% 75% at 62% 35%, var(--blue-glow) 0%, var(--navy) 45%, var(--navy-deep) 100%); }
  .card--back { top: 465px; background:
      linear-gradient(160deg, var(--paper-light) 0%, var(--paper) 60%, #dcdcdc 100%); }

  .card__bands { position: absolute; left: 0; top: 0; width: 700px; height: 400px; }

  .brand { position: absolute; display: flex; align-items: center; gap: 16px; }
  .brand__dot { border-radius: 50%; flex: none; }
  .brand__name { font-weight: 700; line-height: 1; letter-spacing: .5px; white-space: nowrap; }

  .card--front .brand { left: 120px; top: 128px; }
  .card--front .brand__dot { width: 52px; height: 52px; background: var(--white); }
  .card--front .brand__name { color: var(--white); font-size: 44px; }

  .card--front .website {
    position: absolute; right: 60px; bottom: 30px;
    font-weight: 700; font-size: 21px; color: var(--ink); letter-spacing: .5px;
  }

  .card--back .brand { left: 40px; top: 56px; }
  .card--back .brand__dot { width: 36px; height: 36px; background: var(--ink-soft); }
  .card--back .brand__name { color: var(--ink-soft); font-size: 30px; }

  .address {
    position: absolute; left: 40px; top: 148px;
    font-size: 17px; line-height: 1.25; color: var(--ink); font-style: normal;
  }
  .phones {
    position: absolute; left: 40px; top: 204px;
    font-size: 17px; line-height: 1.3; color: var(--ink); list-style: none;
  }
  .phones b { font-weight: 700; }
  .person { position: absolute; right: 50px; top: 176px; color: var(--ink); }
  .person__name { font-size: 21px; }
  .person__title { font-size: 14px; border-left: 1px solid var(--ink); padding-left: 4px; margin-left: 2px; }
  .person__email { font-size: 17px; margin-top: 2px; }
</style>
</head>
<body>
<main class="canvas">

  <section class="card card--front" aria-label="Card front">
    <svg class="card__bands" viewBox="0 0 700 400" aria-hidden="true">
      <defs>
        <linearGradient id="frontSilver" x1="0" x2="1">
          <stop offset="0" stop-color="#ffffff"/>
          <stop offset=".5" stop-color="#e4e6e9"/>
          <stop offset="1" stop-color="#ffffff"/>
        </linearGradient>
      </defs>
      <path d="M0 300 C 200 285, 450 290, 700 302 L700 400 L0 400 Z" fill="var(--rule)"/>
      <path d="M0 308 C 200 293, 450 298, 700 310 L700 400 L0 400 Z" fill="url(#frontSilver)"/>
      <path d="M0 308 C 120 300, 200 320, 260 400 L0 400 Z" fill="var(--silver)" opacity=".45"/>
    </svg>
    <div class="brand">
      <div class="brand__dot"></div>
      <div class="brand__name">LARKSPUR HOMES</div>
    </div>
    <div class="website">www.larkspurhomes.com</div>
  </section>

  <section class="card card--back" aria-label="Card back">
    <svg class="card__bands" viewBox="0 0 700 400" aria-hidden="true">
      <defs>
        <linearGradient id="backBlue" x1="0" x2="1">
          <stop offset="0" stop-color="var(--blue-band)"/>
          <stop offset=".55" stop-color="var(--blue-glow)"/>
          <stop offset="1" stop-color="var(--navy)"/>
        </linearGradient>
      </defs>
      <path d="M0 318 C 220 312, 480 312, 700 318 L700 400 L0 400 Z" fill="var(--rule)"/>
      <path d="M0 326 C 220 320, 480 320, 700 326 L700 400 L0 400 Z" fill="url(#backBlue)"/>
    </svg>
    <div class="brand">
      <div class="brand__dot"></div>
      <div class="brand__name">LARKSPUR HOMES</div>
    </div>
    <address class="address">1475 Birchwood Avenue<br>Lansing, MI 48910</address>
    <ul class="phones">
      <li><b>P:</b> 555-214-3801</li>
      <li><b>F:</b> 555-214-3802</li>
      <li><b>M:</b> 555-214-3803</li>
    </ul>
    <div class="person">
      <div><span class="person__name">Daniel Mercer</span><span class="person__title">President</span></div>
      <div class="person__email">dmercer@larkspurhomes.com</div>
    </div>
  </section>

</main>
</body>
</html>
```